The 50 Year History of the Tallowmere Whippet Coursing Society

The Tallowmere Whippet Coursing Society has been established for 50 years last month. We are putting together a chronological history book with interesting stories about events over the past 50 years.
Book title: Swift Across Decades: 50 Years of the Tallowmere Whippet Coursing Society
Front Cover: We are looking for a simple but striking design. It must have at least one racing greyhound (image from Australia). I can supply images of greyhounds if required. It must have our logo.
Back Cover: can be minimal with club details
Book Size: A4

```html
<!DOCTYPE html>
<html lang="en">
<head>
<meta charset="utf-8">
<title>Swift Across Decades – Cover Spread</title>
<link rel="stylesheet" href="https://fonts.googleapis.com/css2?family=Alfa+Slab+One&family=Graduate&family=Roboto+Condensed:wght@300;500&display=swap">
<style>
  :root {
    --page: #eef1f2;
    --sky: #ece4e6;
    --peach: #e9b89f;
    --dust: #a57a66;
    --earth: #6b5048;
    --night: #2a1f31;
    --hound-light: #9c8c88;
    --hound-dark: #574a4c;
    --plaque: #6a4438;
    --plaque-text: #f8d9c4;
    --ink: #2b1d20;
    --heading: #4a2e28;
    --gold-dark: #6e5630;
    --gold-light: #e7cf79;
    --badge: #3f8a3a;
    --logo: #ffffff;
  }
  * { box-sizing: border-box; margin: 0; padding: 0; }
  html, body { width: 849px; height: 1200px; overflow: hidden; background: var(--page); }
  .spread {
    position: absolute; left: 18px; top: 342px;
    display: flex; gap: 4px; height: 515px;
  }
  .cover, .spine { position: relative; height: 515px; overflow: hidden; }
  .cover { width: 370px; }
  .spine { width: 64px; }
  .photo {
    position: absolute; inset: 0;
    background: linear-gradient(180deg, var(--sky) 0%, var(--peach) 28%, var(--dust) 52%, var(--earth) 70%, var(--night) 86%, var(--night) 100%);
  }
  .hound-photo {
    position: absolute;
    background: radial-gradient(ellipse at 50% 45%, var(--hound-light) 0%, var(--hound-dark) 55%, rgba(87, 74, 76, 0) 75%);
    opacity: 0.85;
  }
  .hound-photo--front { left: 30px; right: 10px; top: 120px; height: 330px; }
  .hound-photo--back { left: 20px; right: 20px; top: 300px; height: 180px; }

  .corner { position: absolute; width: 58px; height: 58px; }
  .corner--tl { top: 0; left: 0; background: var(--gold-dark); }
  .corner--tr { top: 0; right: 0; background: linear-gradient(135deg, var(--gold-light), #b8953f); }
  .corner--bl { bottom: 0; left: 0; background: linear-gradient(45deg, #b8953f, var(--gold-light)); }
  .corner--br { bottom: 0; right: 0; background: var(--gold-dark); }
  .front-panel { position: absolute; inset: 0; border-radius: 40px; overflow: hidden; }

  .subtitle {
    position: absolute; top: 14px; left: 0; right: 0; text-align: center;
    font-family: "Graduate", serif; font-weight: 400; color: var(--ink); line-height: 1.2;
  }
  .subtitle__years { font-size: 36px; display: block; }
  .subtitle__line { font-size: 16px; display: block; margin-top: 3px; }

  .title { position: absolute; top: 168px; left: 0; right: 0; display: flex; flex-direction: column; align-items: center; gap: 6px; }
  .plaque {
    font-family: "Alfa Slab One", serif; font-weight: 400; font-size: 40px; line-height: 1;
    color: var(--plaque-text); text-transform: uppercase;
    padding: 12px 26px 10px;
    text-shadow: 2px 2px 0 #3a211b;
    background:
      radial-gradient(circle at top left, transparent 11px, var(--plaque) 11.5px) top left / 51% 51% no-repeat,
      radial-gradient(circle at top right, transparent 11px, var(--plaque) 11.5px) top right / 51% 51% no-repeat,
      radial-gradient(circle at bottom left, transparent 11px, var(--plaque) 11.5px) bottom left / 51% 51% no-repeat,
      radial-gradient(circle at bottom right, transparent 11px, var(--plaque) 11.5px) bottom right / 51% 51% no-repeat;
  }

  .club-mark {
    position: absolute; bottom: 30px; left: 0; right: 0;
    display: flex; flex-direction: column; align-items: center; gap: 8px;
  }
  .club-mark__dot { width: 26px; height: 26px; border-radius: 50%; background: var(--badge); }
  .club-mark__name {
    width: 220px; text-align: center;
    font-family: "Roboto Condensed", sans-serif; font-weight: 500; font-size: 13px;
    letter-spacing: 1.5px; text-transform: uppercase; color: var(--logo); line-height: 1.35;
  }

  .spine__title {
    position: absolute; left: 50%; top: 50%;
    transform: translate(-50%, -50%) rotate(-90deg);
    white-space: nowrap;
    font-family: "Alfa Slab One", serif; font-weight: 400; font-size: 27px; color: var(--ink);
    text-transform: uppercase; letter-spacing: 1px;
  }

  .details__heading {
    position: absolute; top: 38px; left: 0; right: 0; text-align: center;
    font-family: "Graduate", serif; font-weight: 400; font-size: 30px; color: var(--heading);
  }
  .details__rule { position: absolute; top: 82px; left: 82px; right: 82px; height: 3px; background: var(--heading); }
  .details__box {
    position: absolute; top: 110px; left: 38px; right: 38px; height: 285px;
    padding: 16px; text-align: center;
    font-family: "Roboto Condensed", sans-serif; font-weight: 300; font-size: 11.2px; line-height: 1.45;
    color: var(--plaque-text);
    background:
      radial-gradient(circle at top left, transparent 16px, var(--plaque) 16.5px) top left / 51% 51% no-repeat,
      radial-gradient(circle at top right, transparent 16px, var(--plaque) 16.5px) top right / 51% 51% no-repeat,
      radial-gradient(circle at bottom left, transparent 16px, var(--plaque) 16.5px) bottom left / 51% 51% no-repeat,
      radial-gradient(circle at bottom right, transparent 16px, var(--plaque) 16.5px) bottom right / 51% 51% no-repeat;
  }
</style>
</head>
<body>
  <main class="spread">
    <section class="cover cover--front">
      <div class="corner corner--tl"></div>
      <div class="corner corner--tr"></div>
      <div class="corner corner--bl"></div>
      <div class="corner corner--br"></div>
      <div class="front-panel">
        <div class="photo" role="img" aria-label="Sunset sky over a sandy coursing track"></div>
        <div class="hound-photo hound-photo--front" role="img" aria-label="Photograph of a standing racing greyhound in a red coat, with greyhounds racing along the track below"></div>
        <h2 class="subtitle">
          <span class="subtitle__years">50 Years</span>
          <span class="subtitle__line">of the Tallowmere</span>
          <span class="subtitle__line">Whippet Coursing Society</span>
        </h2>
        <h1 class="title">
          <span class="plaque">Swift</span>
          <span class="plaque">Across</span>
          <span class="plaque">Decades</span>
        </h1>
        <div class="club-mark">
          <span class="club-mark__dot"></span>
          <p class="club-mark__name">Tallowmere Whippet Coursing Society</p>
        </div>
      </div>
    </section>

    <section class="spine">
      <div class="photo" role="img" aria-label="Continuation of the sunset track photograph"></div>
      <p class="spine__title">Swift Across Decades</p>
    </section>

    <section class="cover cover--back">
      <div class="photo" role="img" aria-label="Hazy sky over a dusty coursing track"></div>
      <div class="hound-photo hound-photo--back" role="img" aria-label="Photograph of greyhounds racing along the track"></div>
      <h2 class="details__heading">Club Details</h2>
      <div class="details__rule"></div>
      <div class="details__box">
        <p>Lorem ipsum dolor sit amet, consectetuer adipiscing elit, sed diam nonummy nibh euismod tincidunt ut laoreet dolore magna aliquam erat volutpat. Ut wisi enim ad minim veniam, quis nostrud exerci tation ullamcorper suscipit lobortis nisl ut aliquip ex ea commodo consequat. Duis autem vel eum iriure dolor in hendrerit in vulputate velit esse molestie consequat, vel illum dolore eu feugiat nulla facilisis at vero eros et accumsan et iusto odio dignissim qui blandit praesent luptatum zzril delenit augue duis dolore te feugait nulla facilisi.</p>
        <p>Lorem ipsum dolor sit amet, cons ectetuer adipiscing elit, sed diam nonummy nibh euismod tincidunt ut laoreet dolore magna aliquam erat volutpat. Ut wisi enim</p>
      </div>
      <div class="club-mark">
        <span class="club-mark__dot"></span>
        <p class="club-mark__name">Tallowmere Whippet Coursing Society</p>
      </div>
    </section>
  </main>
</body>
</html>
```